Marisol business card and stationary
business card and stationary
Marisol business card and stationary - Retailers
Creative Brief
Bright & Fun-filled
Janet Wroblenko
owner, designer
marisol a florist 418 north brook lane greenville, sc 29174
info@marisolblooms.example
marisolblooms.example
Concepts
Stationery for Online Retailer

```html
<!DOCTYPE html>
<html lang="en">
<head>
<meta charset="utf-8">
<title>Marisol – Business Card</title>
<link rel="stylesheet" href="https://fonts.googleapis.com/css2?family=Didact+Gothic&display=swap">
<style>
  :root {
    --backdrop: #ece8ea;
    --card-white: #ffffff;
    --card-shade: #f3eef0;
    --rose: #e5426c;
    --rose-light: #f07a97;
    --leaf: #8fae3e;
    --graphite: #6a6a6a;
    --ink: #555555;
  }
  * { box-sizing: border-box; margin: 0; padding: 0; }
  html, body {
    width: 1200px; height: 838px; overflow: hidden;
    background: var(--backdrop);
    font-family: "Didact Gothic", sans-serif;
  }
  .business-card {
    position: absolute; left: 100px; top: 133px;
    width: 1000px; height: 571px;
    background: linear-gradient(180deg, var(--card-white) 0%, var(--card-shade) 100%);
    box-shadow: 0 14px 40px rgba(80, 40, 55, 0.18);
    overflow: hidden;
  }
  .card-wave { position: absolute; inset: 0; width: 1000px; height: 571px; }
  .brand {
    position: absolute; left: 250px; top: 70px;
    display: flex; align-items: center; gap: 22px;
  }
  .brand-dot {
    width: 120px; height: 120px; border-radius: 50%;
    background: radial-gradient(circle, #f6b9c9 0%, var(--rose-light) 100%);
  }
  .brand-name {
    font-size: 62px; color: var(--ink); letter-spacing: 1px; line-height: 1;
  }
  .owner { position: absolute; left: 60px; top: 238px; }
  .owner-name { font-size: 32px; color: var(--rose); font-weight: 400; }
  .owner-role { font-size: 24px; color: var(--ink); margin-top: 4px; }
  .contact {
    position: absolute; right: 50px; bottom: 40px;
    text-align: right; color: var(--card-white);
    font-size: 22px; line-height: 1.5;
  }
  .contact-line { display: flex; justify-content: flex-end; align-items: center; gap: 10px; }
  .contact-icon { width: 20px; height: 20px; }
  .contact-web { font-size: 30px; margin-top: 8px; }
</style>
</head>
<body>
  <main class="business-card">
    <svg class="card-wave" viewBox="0 0 1000 571" aria-hidden="true">
      <defs>
        <linearGradient id="rose-band" x1="0" y1="0" x2="0" y2="1">
          <stop offset="0" stop-color="#ec5b7f"/>
          <stop offset="1" stop-color="#e23b66"/>
        </linearGradient>
      </defs>
      <path d="M0,345 C260,300 560,330 1000,262" fill="none" stroke="#6a6a6a" stroke-width="5"/>
      <path d="M0,360 C280,318 590,340 1000,278" fill="none" stroke="#8fae3e" stroke-width="6"/>
      <path d="M0,385 C300,340 620,360 1000,300 L1000,571 L0,571 Z" fill="url(#rose-band)"/>
    </svg>

    <div class="brand">
      <span class="brand-dot"></span>
      <span class="brand-name">marisol</span>
    </div>

    <div class="owner">
      <p class="owner-name">Janet Wroblenko</p>
      <p class="owner-role">owner, designer</p>
    </div>

    <address class="contact" style="font-style:normal">
      <p>marisol a florist, 418 north</p>
      <p>brook lane, greenville, sc 29174</p>
      <p class="contact-line">
        <svg class="contact-icon" viewBox="0 0 20 20" aria-hidden="true"><path d="M5 2 L8 2 L9 6 L7 8 C8 11 9 12 12 13 L14 11 L18 12 L18 15 C18 17 16 18 14 18 C8 17 3 12 2 6 C2 4 3 2 5 2 Z" fill="#fff"/></svg>
        864.555.0148
      </p>
      <p class="contact-line">
        <svg class="contact-icon" viewBox="0 0 20 20" aria-hidden="true"><rect x="2" y="4" width="16" height="12" fill="none" stroke="#fff" stroke-width="2"/><path d="M2 4 L10 11 L18 4" fill="none" stroke="#fff" stroke-width="2"/></svg>
        info@marisolblooms.example
      </p>
      <p class="contact-web">www.marisolblooms.example</p>
    </address>
  </main>
</body>
</html>
```